Postcard Design

Looking for a postcard to inform of a new email address and inform professionals who refer to us of all our services.

Motto - Working together with families, schools, physicians, and counselors to ensure children exceed

Work with:
Children
Teens
College Students
Adults

Specailize in:
LD
ADHD
IEP
Autism
Tourettes
Depression
Aniexity Disorders
Bi-polar
RAD
Section 504's
Apraxia
Speech Language Disorders
IEE (Independant Education Evaluations)

Target Market(s)

Physicians, Counselors

Industry/Entity Type

College

Logo Text

Vostrand Inc.

Requirements
Must have
• postcard must advertise business/services
postcard must inform past andpotential customers of new email address. vostrand@vostrandinc.kelbimail.com
Nice to have
• list services
Should not have
• Dr. is not a MD. Dr. is a PHD.

```html
<!DOCTYPE html>
<html lang="en">
<head>
<meta charset="utf-8">
<title>Vostrand Inc. — Postcard</title>
<link rel="stylesheet" href="https://fonts.googleapis.com/css2?family=Arvo:wght@400;700&family=Roboto+Condensed:ital,wght@0,400;0,700;1,700&display=swap">
<style>
  :root {
    --bg: #e9e6e2;
    --paper: #ffffff;
    --blue: #0aa6d8;
    --orange: #ef8a2c;
    --purple: #b46eac;
    --green: #5db84a;
    --magenta: #b23b8e;
    --ink: #3a3a3a;
    --ink-soft: #555555;
    --line: #444444;
    --photo-a: #c9a98e;
    --photo-b: #9fb8a4;
    --serif: "Arvo", Georgia, serif;
    --cond: "Roboto Condensed", "Arial Narrow", sans-serif;
    --tile-w: 48.5px;
    --tile-h: 52px;
  }
  * { box-sizing: border-box; margin: 0; padding: 0; }
  html, body { width: 1200px; height: 800px; overflow: hidden; }
  body { background: var(--bg); position: relative; }

  .card {
    position: absolute;
    top: 210px;
    width: 560px;
    height: 380px;
    background: var(--paper);
    box-shadow: 0 4px 14px rgba(0,0,0,.18);
    overflow: hidden;
  }
  .card--back { left: 30px; }
  .card--front { left: 610px; }

  /* ---------- Back side ---------- */
  .mailing-address {
    position: absolute; left: 26px; top: 26px;
    font-family: var(--serif); font-style: normal; font-size: 13px; line-height: 1.55; color: var(--ink-soft);
  }
  .mailing-address .company { color: var(--blue); }
  .divider {
    position: absolute; left: 330px; top: 20px; width: 1px; height: 250px;
    background: var(--line);
  }
  .email-notice {
    position: absolute; left: 40px; width: 295px; top: 282px; text-align: right;
    font-family: var(--cond);
  }
  .email-notice .label { font-size: 11px; color: #111; }
  .email-notice .address { font-size: 16px; font-weight: 700; color: var(--magenta); }
  .color-band span { position: absolute; bottom: 0; }
  .band-purple { left: 0; width: 60px; height: 28px; background: var(--purple); }
  .band-green { left: 60px; width: 160px; height: 28px; background: var(--green); }
  .band-orange { left: 220px; width: 34px; height: 52px; background: var(--orange); }
  .band-blue { left: 254px; width: 66px; height: 52px; background: var(--blue); }

  /* ---------- Front side ---------- */
  .motto-panel {
    position: absolute; left: 0; top: 0; width: 250px; height: 170px;
    background: var(--blue); display: flex; align-items: center; justify-content: center;
  }
  .motto {
    font-family: var(--serif); color: #fff; font-size: 17px; line-height: 1.18; text-align: center;
  }
  .identity { position: absolute; left: 272px; top: 42px; font-family: var(--serif); }
  .identity .company { color: var(--blue); font-size: 17px; letter-spacing: .5px; }
  .identity .person, .identity .role { color: var(--ink); font-size: 12px; line-height: 1.35; }

  .connect { position: absolute; left: 14px; top: 190px; font-family: var(--cond); }
  .connect-title { color: var(--blue); font-weight: 700; font-style: italic; font-size: 12.5px; }
  .connect-rule { display: block; margin: 2px 0 6px; }
  .connect-list { list-style: none; }
  .connect-list li {
    display: flex; align-items: center; gap: 5px;
    font-size: 10px; font-weight: 700; color: var(--ink); margin-bottom: 5px;
  }
  .dot { width: 11px; height: 11px; border-radius: 50%; flex: none; }
  .dot--purple { background: var(--purple); }
  .dot--navy { background: #3b5a9a; }
  .dot--red { background: #d0393e; }

  /* Service mosaic: 7 columns × 4 rows, bottom-right of the front */
  .services { position: absolute; left: 220px; top: 172px; width: 340px; height: 208px; }
  .tile {
    position: absolute;
    left: calc(var(--c) * var(--tile-w));
    top: calc(var(--r) * var(--tile-h));
    width: calc(var(--w, 1) * var(--tile-w));
    height: var(--tile-h);
    display: flex; flex-direction: column; align-items: center; justify-content: center; text-align: center;
    font-family: var(--cond); font-weight: 700; color: #fff; font-size: 10px; line-height: 1.1;
    padding: 2px;
  }
  .tile--dense { font-size: 9px; }
  .tile .tile-note { display: block; font-size: 7px; line-height: 1.1; margin-top: 2px; }
  .tile--orange { background: var(--orange); }
  .tile--blue { background: var(--blue); }
  .tile--purple { background: var(--purple); }
  .tile--green { background: var(--green); }
  .tile--photo { background: linear-gradient(135deg, var(--photo-a), var(--photo-b)); }
</style>
</head>
<body>

<section class="card card--back" aria-label="Postcard back">
  <address class="mailing-address">
    <div class="company">Vostrand Inc.</div>
    <div>2240 Halden Road</div>
    <div>Suite 210</div>
    <div>Marlow Falls, NY 14000</div>
    <div>(555) 014-2290</div>
  </address>
  <div class="divider"></div>
  <div class="email-notice">
    <div class="label">Please note new email address</div>
    <div class="address">vostrand@vostrandinc.kelbimail.com</div>
  </div>
  <div class="color-band">
    <span class="band-purple"></span><span class="band-green"></span>
    <span class="band-orange"></span><span class="band-blue"></span>
  </div>
</section>

<section class="card card--front" aria-label="Postcard front">
  <div class="motto-panel">
    <p class="motto">Working together<br>with families,<br>schools, physicians,<br>and counselors<br>to ensure children<br>exceed</p>
  </div>

  <div class="identity">
    <div class="company">VOSTRAND INC</div>
    <div class="person">Nolan R. Vostrand, Ph.D</div>
    <div class="role">Education Specialist</div>
  </div>

  <div class="connect">
    <div class="connect-title">Connect with Vostrand Inc at</div>
    <svg class="connect-rule" width="160" height="6" viewBox="0 0 160 6"><path d="M0 5 Q80 -1 160 3" stroke="#0aa6d8" stroke-width="1.5" fill="none"/></svg>
    <ul class="connect-list">
      <li><svg width="11" height="11" viewBox="0 0 12 12"><circle cx="6" cy="6" r="6" fill="#0aa6d8"/><rect x="3" y="4" width="6" height="4.2" fill="none" stroke="#fff" stroke-width=".8"/><path d="M3 4 L6 6.4 L9 4" fill="none" stroke="#fff" stroke-width=".8"/></svg>vostrand@vostrandinc.kelbimail.com</li>
      <li><span class="dot dot--purple"></span>vostrandinc.kelbi.com</li>
      <li><span class="dot dot--navy"></span>Vostrand-Inc/270418836512</li>
      <li><span class="dot dot--red"></span>Drvostrand</li>
    </ul>
  </div>

  <div class="services">
    <div class="tile tile--orange" style="--c:1;--r:0">LD</div>
    <div class="tile tile--photo" style="--c:2;--r:0;--w:2" role="img" aria-label="Photo of young children lying on grass"></div>
    <div class="tile tile--purple" style="--c:4;--r:0">ADHD</div>
    <div class="tile tile--blue" style="--c:5;--r:0">IEP</div>
    <div class="tile tile--photo" style="--c:6;--r:0" role="img" aria-label="Photo of a college student holding books"></div>

    <div class="tile tile--photo" style="--c:0;--r:1" role="img" aria-label="Photo of two smiling teenage girls"></div>
    <div class="tile tile--blue" style="--c:1;--r:1">Tourettes</div>
    <div class="tile tile--photo" style="--c:2;--r:1;--w:2" role="img" aria-label="Photo of a group of children in a circle"></div>
    <div class="tile tile--orange tile--dense" style="--c:4;--r:1">Depression</div>
    <div class="tile tile--blue tile--dense" style="--c:5;--r:1">Anxiety Disorders</div>
    <div class="tile tile--green" style="--c:6;--r:1">Autism</div>

    <div class="tile tile--green" style="--c:0;--r:2">RAD</div>
    <div class="tile tile--purple" style="--c:1;--r:2">Section 504's</div>
    <div class="tile tile--blue tile--dense" style="--c:2;--r:2">Motor Coordination Disorders</div>
    <div class="tile tile--photo" style="--c:3;--r:2;--w:2" role="img" aria-label="Photo of a smiling adult couple"></div>
    <div class="tile tile--blue" style="--c:5;--r:2"></div>
    <div class="tile tile--purple" style="--c:6;--r:2">Bi-polar</div>

    <div class="tile tile--purple" style="--c:4;--r:3;--w:2">Speech Language Disorders</div>
    <div class="tile tile--orange" style="--c:6;--r:3">IEE<span class="tile-note">(Independent Education Evaluations)</span></div>
  </div>
</section>

</body>
</html>
```